Larkspur Ridge Management - Business Cards

I need business cards. My current logo was designed by a designer at this site and I very much like and am happy with the results. I would like a business card that is trendy, unique, current yet professional. I deal with high net worth clients daily

Target Market(s)

Out of state investors looking to get into the rental market in Ohio

Industry/Entity Type

Property Management, Consulting

Contact Information for Business Card

Name, Title (Chief Financial Officer) office phone number (555) 817-3094 website address larkridgemgmt.example

Font styles to use
Sans Serif

Colors
0054AA
0677BA
7BADD7
CADEEF
E8F1F8
0094D4
00A9DD
6FCCEA
C7EBF8
E9F6FB
00AB8E
00BBA5
67D7C9
C6EFE9
E9F9F6

```html
<!DOCTYPE html>
<html lang="en">
<head>
<meta charset="utf-8">
<title>Larkspur Ridge Management – Business Card</title>
<link rel="stylesheet" href="https://fonts.googleapis.com/css2?family=Bebas+Neue&family=Lato:wght@400&display=swap">
<style>
  :root {
    --page: #ffffff;
    --card: #ffffff;
    --card-edge: #dcdcdc;
    --navy: #2d3e62;
    --red: #ed2024;
    --red-deep: #b31a22;
    --ink: #000000;
    --white: #ffffff;
  }
  * { margin: 0; padding: 0; box-sizing: border-box; }
  html, body {
    width: 1200px; height: 1200px; overflow: hidden;
    background: var(--page);
  }
  .canvas { position: relative; width: 1200px; height: 1200px; }
  .business-card {
    position: absolute; left: 309px; top: 340px;
    width: 612px; height: 373px;
    background: var(--card);
    border: 1px solid var(--card-edge);
    box-shadow: 4px 6px 8px rgba(0,0,0,0.08);
    overflow: hidden;
  }
  .card-graphics { position: absolute; inset: 0; }
  .brand-name {
    position: absolute; left: 22px; top: 108px; width: 240px;
    display: flex; align-items: flex-start; gap: 10px;
    font-family: "Bebas Neue", sans-serif;
    font-size: 40px; line-height: 0.95;
    color: var(--navy);
  }
  .brand-mark {
    flex: none; width: 22px; height: 22px; margin-top: 6px;
    background: var(--navy);
  }
  .title {
    position: absolute; left: 359px; top: 66px;
    font-family: "Bebas Neue", sans-serif;
    color: var(--ink); line-height: 0.86;
  }
  .title-lead { display: block; font-size: 33px; }
  .title-main { display: block; font-size: 62px; letter-spacing: -0.5px; }
  .phone {
    position: absolute; left: 361px; top: 226px;
    font-family: "Bebas Neue", sans-serif;
    font-size: 26px; color: var(--ink);
  }
  .website {
    position: absolute; left: 359px; top: 262px;
    font-family: "Lato", sans-serif;
    font-size: 21px; color: var(--ink);
  }
</style>
</head>
<body>
<div class="canvas">
  <div class="business-card">
    <svg class="card-graphics" width="612" height="373" viewBox="0 0 612 373" aria-hidden="true">
      <rect class="base-band" x="0" y="297" width="612" height="47" fill="var(--navy)"/>
      <rect class="accent-stripe" x="288" y="0" width="45" height="297" fill="var(--red)"/>
      <polygon class="accent-arrow" points="223,297 397,297 311,344" fill="var(--red)"/>
      <rect class="phone-tile" x="288" y="218" width="45" height="39" fill="var(--red-deep)"/>
      <!-- person icon -->
      <circle cx="311" cy="109" r="6" fill="var(--white)"/>
      <path d="M302 126 v-4 a9 6 0 0 1 18 0 v4 z" fill="var(--white)"/>
      <!-- phone icon -->
      <path d="M302 229 l4 -3 l5 7 l-3 2 q3 6 9 10 l2 -3 l7 5 l-3 4 q-16 -4 -21 -22 z" fill="var(--white)"/>
      <!-- envelope icon -->
      <rect x="302" y="268" width="18" height="13" fill="none" stroke="var(--white)" stroke-width="1.6"/>
      <path d="M302 268 l9 8 l9 -8 M302 281 l6 -6 M320 281 l-6 -6" fill="none" stroke="var(--white)" stroke-width="1.4"/>
    </svg>

    <div class="brand-name">
      <span class="brand-mark"></span>
      <span>Larkspur Ridge<br>Management</span>
    </div>

    <h1 class="title">
      <span class="title-lead">Chief</span>
      <span class="title-main">Financial</span>
      <span class="title-main">Officer</span>
    </h1>
    <p class="phone">(555) 817-3094</p>
    <p class="website">larkridgemgmt.example</p>
  </div>
</div>
</body>
</html>
```